Fresh Start Credit Guide - Banner Ad for CA Website

I need a banner ad for a book I'm selling.

The book is about Fresh Start Credit Guide, that is a County Court Judgment, from a credit report.

I have two websites. I want the banner ad to appear on
www.cardenashby.co.uk

It will then link to the new site: https://freshstartcreditguide.co.uk/

The first site already has a lot of traffic from visitors wanting to remove a CCJ. The purpose of that first site was originally for visitors to become clients of the law firm. However, most visitors can't afford legal advice and so I'd like to offer them the book instead.

I would like to see designs that use the colour green. The final design should communicate financial freedom, simplicity and trustworthiness.

Target Market(s)

Individuals who have discovered a CCJ on their credit report

Industry/Entity Type

Law

Font styles to use
Sans Serif

Colors
0054AA
0677BA
7BADD7
CADEEF
E8F1F8
0094D4
00A9DD
6FCCEA
C7EBF8
E9F6FB
00AB8E
00BBA5
67D7C9
C6EFE9
E9F9F6

Requirements
Must have
• Must fit at the end of a blog article, such as this one https://www.cardenashby.co.uk/ccj-wrong-address/

```html
<!DOCTYPE html>
<html lang="en">
<head>
<meta charset="utf-8">
<title>Fresh Start Credit Guide – Banner</title>
<link href="https://fonts.googleapis.com/css2?family=Montserrat:wght@400;700;800&display=swap" rel="stylesheet">
<style>
  :root {
    --stage: #8d8d8d;
    --green: #43a047;
    --green-light: #53b257;
    --green-shadow: #2b7a30;
    --orange: #f29a12;
    --yellow: #ffd270;
    --white: #ffffff;
    --product-light: #f7f5f2;
    --product-mid: #e6e1dc;
  }
  * { margin: 0; padding: 0; box-sizing: border-box; }
  html, body { width: 1200px; height: 800px; overflow: hidden; }
  body {
    background: var(--stage);
    font-family: "Montserrat", sans-serif;
    position: relative;
  }
  .banner {
    position: absolute;
    left: 94px; top: 192px;
    width: 1012px; height: 416px;
    overflow: hidden;
    background: var(--yellow);
  }
  .banner-shapes { position: absolute; inset: 0; }
  .headline {
    position: absolute;
    left: 58px; top: 28px;
    color: var(--white);
    font-weight: 800;
    line-height: 1;
    text-shadow: 3px 3px 0 var(--green-shadow);
  }
  .headline-lead { display: block; font-size: 46px; margin-left: 68px; }
  .headline-main { display: block; font-size: 86px; margin-top: -6px; letter-spacing: -1px; }
  .headline-end { display: block; font-size: 95px; margin-top: -8px; margin-left: 40px; letter-spacing: -1px; position: relative; }
  .headline-end .article { font-size: 34px; position: absolute; left: -30px; top: 4px; }
  .tagline {
    position: absolute;
    left: 64px; top: 243px;
    padding-left: 16px;
    border-left: 3px solid var(--white);
    color: var(--white);
    font-size: 22px;
    line-height: 1.25;
  }
  .tagline strong { font-weight: 700; display: block; }
  .tagline span { font-weight: 400; display: block; padding-left: 4px; }
  .cta {
    position: absolute;
    left: 64px; top: 323px;
    width: 283px; height: 51px;
    border: 2px solid var(--white);
    border-radius: 26px;
    background: var(--orange);
    color: var(--white);
    font-weight: 700;
    font-size: 23px;
    display: flex; align-items: center; justify-content: center;
    text-decoration: none;
  }
  .product-visual {
    position: absolute;
    left: 509px; top: 31px;
    width: 450px; height: 352px;
    border-radius: 10px;
    background: linear-gradient(135deg, var(--product-light), var(--product-mid));
  }
</style>
</head>
<body>
  <a class="banner" href="https://freshstartcreditguide.co.uk/" aria-label="Fresh Start Credit Guide">
    <svg class="banner-shapes" width="1012" height="416" viewBox="0 0 1012 416" aria-hidden="true">
      <polygon points="459,0 533,0 760,416 716,416" fill="var(--orange)"/>
      <polygon points="0,0 459,0 716,416 0,416" fill="var(--green)"/>
      <polygon points="0,220 214,416 0,416" fill="var(--green-light)"/>
    </svg>
    <h1 class="headline">
      <span class="headline-lead">Need to</span>
      <span class="headline-main">Remove</span>
      <span class="headline-end"><span class="article">a</span>CCJ?</span>
    </h1>
    <p class="tagline">
      <strong>Find out how with this simple</strong>
      <span>jargon-free guide</span>
    </p>
    <span class="cta">Get Your Copy Now</span>
    <div class="product-visual" role="img" aria-label="Fresh Start Credit Guide by Daniel Hartley, shown as a paperback, a tablet and a phone"></div>
  </a>
</body>
</html>
```